photowall advertisement

We require a wall featuring our company logo. We would like to avoid the color green, and gold is highly preferred. The design should be similar to the one in the attached photo. The wall will be used for photos and promotional purposes during congresses. Files must be prepared for printing.
dimension of wall: 470x223 cm

Industry/Entity Type

lifestyle

Colors
0054AA
0677BA
7BADD7
CADEEF
E8F1F8
6B429C
8869AF
B7A5CE
E3DAEB
F3F0F8

Requirements
Must have
• gold color, white, and other compare with gold color
Nice to have
• some pictograms, maps of Europe

```html
<!DOCTYPE html>
<html lang="en">
<head>
<meta charset="utf-8">
<title>Vela Axis Technology – Photo Wall</title>
<link href="https://fonts.googleapis.com/css2?family=Michroma&display=swap" rel="stylesheet">
<style>
  :root {
    --page-bg: #ffffff;
    --wall-black: #0b0b0d;
    --panel-dark: #15161a;
    --panel-mid: #1b1c21;
    --gold-light: #f8dd82;
    --gold-soft: #e9d57a;
    --gold-deep: #a8781f;
    --gold-line: #d9a943;
    --text-white: #ffffff;
    --text-dark: #141414;
  }
  html, body {
    margin: 0;
    width: 927px;
    height: 1200px;
    overflow: hidden;
    background: var(--page-bg);
  }
  .canvas {
    position: relative;
    width: 927px;
    height: 1200px;
    display: flex;
    align-items: center;
    justify-content: center;
  }
  .photo-wall {
    width: 860px;
    height: 408px;
    display: block;
    box-shadow: 0 6px 14px rgba(0,0,0,0.35);
  }
  .brand-text {
    font-family: "Michroma", sans-serif;
    font-weight: 400;
  }
</style>
</head>
<body>
<main class="canvas">
  <svg class="photo-wall" viewBox="0 0 1265 600" xmlns="http://www.w3.org/2000/svg" aria-label="Vela Axis Technology photo wall">
    <defs>
      <linearGradient id="goldFill" x1="0" y1="0" x2="0" y2="1">
        <stop offset="0" stop-color="var(--gold-light)"/>
        <stop offset="1" stop-color="var(--gold-soft)"/>
      </linearGradient>
      <linearGradient id="goldStroke" x1="0" y1="0" x2="1" y2="1">
        <stop offset="0" stop-color="var(--gold-deep)"/>
        <stop offset="0.5" stop-color="#f6d06a"/>
        <stop offset="1" stop-color="var(--gold-deep)"/>
      </linearGradient>
      <linearGradient id="cityTone" x1="0" y1="0" x2="0" y2="1">
        <stop offset="0" stop-color="#1a1b1f"/>
        <stop offset="0.5" stop-color="#26272b"/>
        <stop offset="1" stop-color="#101013"/>
      </linearGradient>
      <clipPath id="wallClip"><rect width="1265" height="600"/></clipPath>
    </defs>

    <g clip-path="url(#wallClip)">
      <rect class="wall-background" width="1265" height="600" fill="var(--wall-black)"/>

      <!-- background hexagon panels -->
      <g class="backdrop-panels">
        <polygon points="180,0 400,0 520,220 400,430 180,430 70,220" fill="var(--panel-dark)"/>
        <polygon points="185,30 325,30 375,120 325,210 185,210 135,120" fill="var(--panel-mid)"/>
        <polygon points="900,380 1140,380 1260,600 1140,820 900,820 780,600" fill="var(--panel-dark)"/>
        <polygon points="990,0 1265,0 1265,300 1100,300" fill="#111215"/>
        <polygon points="0,380 200,380 300,600 0,600" fill="#121316"/>
        <polygon points="300,0 960,0 1050,300 960,600 300,600 220,300" fill="#101114"/>
      </g>

      <!-- central frame -->
      <polygon class="frame-band" points="322,300 470,30 800,30 938,300 790,570 470,570" fill="#1c1d22"/>
      <polygon class="city-panel" role="img" aria-label="Night skyline photograph of a city seen from above"
               points="340,300 482,45 790,45 922,300 775,555 482,555" fill="url(#cityTone)"/>
      <polygon class="frame-line" points="336,300 480,42 792,42 926,300 777,558 480,558"
               fill="none" stroke="url(#goldStroke)" stroke-width="3"/>

      <!-- wordmark -->
      <g class="wordmark brand-text" fill="var(--text-white)" text-anchor="middle">
        <text x="630" y="302" font-size="44" letter-spacing="3">VELA AXIS</text>
        <text x="630" y="330" font-size="14" letter-spacing="9">TECHNOLOGY</text>
      </g>

      <!-- gold hexagon accents -->
      <g class="accent-hexes">
        <polygon class="hex-solid" points="40,300 84,222 172,222 217,300 172,378 84,378" fill="url(#goldFill)"/>
        <text class="brand-text" x="128" y="316" font-size="42" text-anchor="middle" fill="var(--text-dark)">VA</text>

        <polygon class="hex-outline" points="268,452 285,422 319,422 336,452 319,482 285,482"
                 fill="none" stroke="url(#goldStroke)" stroke-width="6"/>
        <polygon class="hex-outline" points="78,555 109,500 171,500 202,555 171,610 109,610"
                 fill="none" stroke="url(#goldStroke)" stroke-width="8"/>
        <polygon class="hex-outline" points="930,30 948,0 982,0 1000,30 982,58 948,58"
                 fill="none" stroke="url(#goldStroke)" stroke-width="6"/>

        <polygon class="hex-outline" points="1053,150 1084,97 1146,97 1177,150 1146,203 1084,203"
                 fill="#0d0d10" stroke="url(#goldStroke)" stroke-width="8"/>
        <text class="brand-text" x="1115" y="157" font-size="18" text-anchor="middle" fill="var(--text-white)">AXIS</text>

        <polygon class="hex-solid" points="1048,470 1094,392 1186,392 1228,470 1186,548 1094,548" fill="url(#goldFill)"/>
        <text class="brand-text" x="1138" y="483" font-size="34" text-anchor="middle" fill="var(--text-dark)">VELA</text>
      </g>
    </g>
  </svg>
</main>
</body>
</html>
```